"Lantern Field" Play - Poster Design for Theatre Group

We are an amateur theatre group based in Geneva, Switzerland. We take pride in eye-catching posters for our shows, which are printed in various sizes.
This design will be for a play in March 2016. The play is called "Lantern Field", and it's a Harwick Medal winner from Marcus Ellery-Pound. The play is about a couple who have everything a family could want, until they lose a child in a life-shattering accident that turns their world upside down. The play charts the couple's bittersweet search to find each other and to find comfort.
Most importantly, we want a design that will make people want to see the show. We don't want to give away the plot or be too heavy-handed about death, but we want it to be clear that it's not a comedy (although there are some lighter moments!).
Attached you will find a template for the poster. This simply has our group name and logo in the top right corner: (Lakeshore Stage Players Circle presents).
You may change the color of both the text and the logo, but please do not change the font, size, or location.
Here is the information that needs to be on the poster, wherever you see fit:
play title: Lantern Field
author byline: by Marcus Ellery-Pound
director line: directed by Rob Feltwick
tagline: How do you keep it together when your whole world's fallen apart?
dates and times:
1-5 March 2016
(Tue-Fri 20:00, Sat 19:00)
location:
Théâtre du Vieux-Moulin
Eaux-Vives, Geneva
websites:
www.lspc.ch
www.scenelettres.ch
Technical Details:
Any font or combination of fonts is acceptable. The largest text should be the play title. The author's name must be at least 50% of the title font size.
For this competition, we would like the version with A3 proportions, which will also be used at F4 (89.5 x 128 cm) and A5 sizes (14.8 x 21 cm). Therefore no text should be below 9pt at A5.
However, from the winning designer we will also need repurposed sizes of the same design. Here is a comprehensive list of the sizes we will need.
1) A3 print poster. Artwork should be 300dpi, CMYK, sent with a 1mm bleed all round, to specification PDF/X-1A:2001. We will need this image in PDF format in addition to the default Artbrigade formats.
2) Chatterly advert picture. 1200px by 628px, RGB jpeg. This must comply with Chatterly’s restrictions on amount of text, which is no more than 20% of area taken up by text.(https://www.chatterly.example/ads/tools/text_overlay).
Because of these restrictions it is sufficient to include just the title and the author's name in this version.
3) Chatterly cover picture: 851px by 314px. RGB jpeg. It is sufficient to include just the title and the author's name in this version.
4) Web banner. 1000px by 300px. RGB jpeg. This version should include just the main image(s), no text.
Theatergoers
Entertainment

```html
<!DOCTYPE html>
<html lang="en">
<head>
<meta charset="utf-8">
<title>Lantern Field – Poster</title>
<link href="https://fonts.googleapis.com/css2?family=League+Gothic&family=Oswald:wght@500;600&family=Fira+Sans+Condensed:wght@500;600;700&display=swap" rel="stylesheet">
<style>
  :root {
    --stage-yellow: #fdc91f;
    --ink: #231f20;
    --paper: #ffffff;
    --backdrop: #e4e4e2;
  }
  * { margin: 0; padding: 0; box-sizing: border-box; }
  html, body {
    width: 960px;
    height: 1200px;
    overflow: hidden;
    background: var(--backdrop);
  }
  .poster {
    position: absolute;
    left: 64px;
    top: 12px;
    width: 832px;
    height: 1176px;
    overflow: hidden;
    background: var(--stage-yellow);
    color: var(--ink);
    font-family: "Fira Sans Condensed", "Arial Narrow", sans-serif;
  }
  .presenter {
    position: absolute;
    top: 34px;
    right: 52px;
    display: flex;
    align-items: center;
    gap: 14px;
  }
  .presenter-name {
    text-align: right;
    font-weight: 700;
    font-size: 21px;
    line-height: 1.12;
  }
  .presenter-mark {
    width: 62px;
    height: 62px;
    border: 5px solid var(--ink);
    border-radius: 50%;
  }
  .key-art {
    position: absolute;
    left: 112px;
    top: 280px;
    width: 620px;
    height: 340px;
  }
  .title {
    position: absolute;
    top: 676px;
    left: 0;
    width: 100%;
    text-align: center;
    white-space: nowrap;
    font-family: "League Gothic", "Oswald", sans-serif;
    font-weight: 400;
    font-size: 168px;
    line-height: 0.9;
    letter-spacing: 1px;
    text-transform: uppercase;
  }
  .title-light { color: var(--paper); }
  .tagline {
    position: absolute;
    top: 862px;
    left: 92px;
    width: 648px;
    padding: 10px 0 9px;
    background: var(--ink);
    color: var(--stage-yellow);
    text-align: center;
    font-weight: 600;
    font-size: 24px;
    line-height: 1.22;
    text-transform: uppercase;
  }
  .credits {
    position: absolute;
    top: 956px;
    left: 0;
    width: 100%;
    text-align: center;
    font-family: "Oswald", sans-serif;
    font-weight: 500;
    text-transform: uppercase;
    white-space: nowrap;
  }
  .credits .role { font-size: 24px; }
  .credits .person { font-size: 38px; letter-spacing: -0.5px; }
  .details {
    position: absolute;
    top: 1030px;
    left: 0;
    width: 100%;
    text-align: center;
    font-weight: 500;
    font-size: 20px;
    line-height: 1.3;
  }
  .details .dates { font-weight: 700; font-size: 21px; }
  .details .venue { text-transform: uppercase; }
</style>
</head>
<body>
  <main class="poster">
    <header class="presenter">
      <p class="presenter-name">Lakeshore Stage<br>Players Circle<br>presents</p>
      <span class="presenter-mark" aria-hidden="true"></span>
    </header>

    <svg class="key-art" viewBox="0 0 620 340" role="img"
         aria-label="Illustration: two facing head silhouettes, a woman and a man, each with a tiny figure on a tightrope across the head">
      <defs>
        <linearGradient id="keyArtTone" x1="0" y1="0" x2="1" y2="1">
          <stop offset="0" stop-color="#2b2622"/>
          <stop offset="1" stop-color="#3a332a"/>
        </linearGradient>
      </defs>
      <rect width="620" height="340" rx="28" fill="url(#keyArtTone)"/>
    </svg>

    <h1 class="title">Lantern<span class="title-light">Field</span></h1>

    <p class="tagline">How do you keep it together<br>when your whole world's fallen apart?</p>

    <p class="credits">
      <span class="role">By</span> <span class="person">Marcus Ellery-Pound</span>
      <span class="role">Directed by</span> <span class="person">Rob Feltwick</span>
    </p>

    <div class="details">
      <p class="dates">1-5 MARCH 2016 (TUE-FRI 20:00, SAT 19:00)</p>
      <p class="venue">Théâtre du Vieux-Moulin, Eaux-Vives, Geneva</p>
      <p class="sites">www.lspc.ch&nbsp; | &nbsp;www.scenelettres.ch</p>
    </div>
  </main>
</body>
</html>
```